Web design for facial expression recognition service

We offer a service which allows customers to film large panels of participants looking at some video/screen (e.g. an advertisement) and to analyze the facial expressions shown by the participants. We are looking for the design of a new website which will make it easy for our customers to setup and view the results of these experiments online.
Competitor's websites that may serve as a reference are:
http://www.moravelt.example/pindor/#pane_overview
http://www.quintabrook.example/homepage.aspx
https://www.tavorlin.example/
The website will (for as far as the design is concerned) consist of three parts:
- A public home page (and perhaps some contact/news/about page), designed to catch the attention/interest potential customers.
- A (protected) project result page, showing the results in an interactive page with charts and numerical data.
- Pages (also protected) with fields and tables (setting up the project details).
The winner of this design project should provide us with at least one design for each of the above in order to get a complete 'theme' going which our developers can use. However, you are welcome to initially only provide the design for the project result page and/or home page.
We are looking for a modern, fresh, yet professional look (my client is a more established party in the field).
The final delivery should consist of layered Photoshop or Illustrator files.
Thank you in advance for participating!
Dear designers,
Reason: Extending the deadline by a few days to give designers a chance to submit designs for the other pages and process further feedback.
Target Market(s)
marketing research agencies (B2B service)
Industry/Entity Type
Delivery
Requirements
Must have
- Home page:
- Basic advertisement of the service; some quick explanation of how it works
- A way to login for existing users
- A link/button/banner inviting people to sign up
- Navigation controls to 2-3 other pages
- Social media links (Chatterbay, WorkNest group)
- Company logo (sorry, can't provide it as my client wishes to remain anonymous for now, but it's rounded and has blue as it's main color).
- Copyright / creator details
Project result page:
(see attachment 1 for a functional mockup - the design may follow this layout closely, or be completely different)
- Title
- A video player and basic numerical data
- Different views of the analysis results can dynamically be added/removed/collapsed/expanded; each one of these views will show some kind of chart, filters (combos), numerical data and a download button/link.
- A way to sign out, go to the main project page and go to the main page
- Logo
- Copyright
The form pages:
(see attachment 2 for a functional mockup of one of the pages; feel free to change some elements to better show the overall style)
- Title
- Text fields, combos, calendar pickers, tables, navigation links
- Logo
- Copyright
Nice to have
- Any creative text elements or product logo/symbol are a bonus. However, the basic "Lorem Ipsum" would do too.

```html
<!DOCTYPE html>
<html lang="en">
<head>
<meta charset="utf-8">
<title>gazemetric – Media Files</title>
<link rel="stylesheet" href="https://fonts.googleapis.com/css2?family=Arimo:wght@400;700&family=Rokkitt:wght@300;400&display=swap">
<style>
:root{
  --brand-blue:#0b7af2;
  --brand-blue-dark:#0866cf;
  --nav-black:#1d1d1d;
  --side-dark:#252525;
  --side-lower:#303030;
  --page-bg:#e3e3e3;
  --panel-bg:#d3d3d3;
  --ink:#333;
  --ink-soft:#555;
  --muted:#777;
  --link:#1a82e2;
  --field-bg:#f7f7f7;
  --field-line:#c4c4c4;
  --rule:#cfcfcf;
  --footer-bg:#242424;
}
*{box-sizing:border-box;margin:0;padding:0}
html,body{width:868px;height:1200px;overflow:hidden}
body{position:relative;background:var(--page-bg);font-family:"Arimo",Arial,sans-serif;color:var(--ink);font-size:9px}
.abs{position:absolute}

.top-band{left:0;top:0;width:868px;height:53px;background:var(--brand-blue);border-bottom:3px solid var(--brand-blue-dark)}
.brand{left:94px;top:17px;color:#fff;font-size:20px;font-weight:700;letter-spacing:-.5px}
.main-nav{left:0;top:53px;width:868px;height:41px;background:var(--nav-black)}
.main-nav .item{position:absolute;top:15px;color:#fff;font-size:10px;font-weight:700}
.user-avatar{left:698px;top:64px;width:20px;height:20px;background:#8a8a8a;border:1px solid #aaa}
.user-caret{left:785px;top:67px;width:13px;height:13px;background:#000;border-radius:2px}

.sidebar{left:0;top:94px;width:59px;height:992px;background:var(--side-dark)}
.sidebar-lower{left:0;top:1082px;width:59px;height:118px;background:var(--side-lower)}
.notch{left:46px;width:0;height:0;border-top:11px solid transparent;border-bottom:11px solid transparent;border-right:13px solid #cfcfcf}

.page-title{left:130px;top:126px;font-family:"Rokkitt",Georgia,serif;font-weight:300;font-size:27px;color:#444}
.breadcrumb{left:130px;top:169px;font-size:9px;color:#333}
.breadcrumb a{color:var(--link);text-decoration:none}
.rule{left:90px;width:762px;height:2px;border-top:1px solid var(--rule);border-bottom:1px solid #f2f2f2}

.section-title{left:112px;font-size:14px;font-weight:700;color:#3a3a3a}
.section-desc{left:112px;font-size:7.5px;color:#444}

.label{font-size:8px;color:#444;text-align:right}
.field{height:24px;background:var(--field-bg);border:1px solid var(--field-line);border-radius:2px;font-size:8px;color:#777;padding:7px 7px}
.field.focus{border-color:#8fb8e8;box-shadow:0 0 3px #9cc3f0;color:#333}
.btn{height:22px;background:linear-gradient(#fafafa,#e6e6e6);border:1px solid #b9b9b9;border-radius:2px;font-size:8px;font-weight:700;color:#333;text-align:center;line-height:20px}

.stimuli-table{left:132px;top:553px;width:656px;border-collapse:collapse;border:1px solid #c9c9c9;font-size:8.5px;color:#555}
.stimuli-table th{height:36px;background:linear-gradient(#fdfdfd,#ececec);font-weight:400;color:#333;border-right:1px solid #d2d2d2;border-bottom:2px solid #cfcfcf}
.stimuli-table td{height:34px;text-align:center;border-right:1px solid #d4d4d4}
.stimuli-table tr.odd td{background:#e9e9e9}
.stimuli-table tr.even td{background:#e1e1e1}
.row-action{color:var(--link);text-decoration:underline;font-size:8px}
.ico{display:inline-block;width:8px;height:9px;vertical-align:-1px;margin-right:3px}

.add-panel{left:132px;top:680px;width:656px;height:82px;background:var(--panel-bg);border:1px solid #c8c8c8}
.panel-label{font-size:8px;color:#444}
.time-box{width:19px;height:20px;background:#fff;border:1px solid #c4c4c4;border-radius:2px;font-size:8px;text-align:center;line-height:18px;color:#555}
.unit{font-size:8px;color:#555}

.check{width:11px;height:11px;background:#d2d2d2;border:1px solid #c0c0c0}
.check-label{font-size:8.5px;color:#333}

.site-footer{left:59px;top:1086px;width:809px;height:114px;background:var(--footer-bg)}
.social{top:1135px;width:12px;height:12px;background:#555}
.footer-brand{left:697px;top:1130px;color:#fff;font-size:17px;font-weight:700;letter-spacing:-.5px}
.footer-link{top:1164px;font-size:8.5px;color:#4a8fe0}
.copyright{left:716px;top:1165px;font-size:7.5px;color:#555}
</style>
</head>
<body>

<header>
  <div class="abs top-band"></div>
  <div class="abs brand">gazemetric</div>
  <nav class="abs main-nav">
    <svg class="abs" style="left:128px;top:12px" width="16" height="15" viewBox="0 0 16 15" aria-label="Home"><path d="M8 1 L15 7 H13 V14 H9.5 V10 H6.5 V14 H3 V7 H1 Z" fill="#fff"/></svg>
    <span class="item" style="left:198px">Projects <span style="font-weight:400;margin-left:6px">▾</span></span>
    <span class="item" style="left:278px">Result</span>
    <span class="item" style="left:353px">Submit your Project</span>
    <span class="item" style="left:492px">Help</span>
    <span class="item" style="left:728px">Alan Merrow</span>
  </nav>
  <div class="abs user-avatar" role="img" aria-label="User avatar"></div>
  <div class="abs user-caret"><svg width="13" height="13"><path d="M4 5 H9 L6.5 8 Z" fill="#fff"/></svg></div>
</header>

<aside>
  <div class="abs sidebar"></div>
  <div class="abs sidebar-lower"></div>
  <div class="abs notch" style="top:241px"></div>
  <div class="abs notch" style="top:501px"></div>
  <div class="abs notch" style="top:812px"></div>
</aside>

<main>
  <h1 class="abs page-title">Lorem ipsum dolor sit amet</h1>
  <div class="abs breadcrumb"><a href="#">Home</a> &nbsp;/&nbsp; <a href="#">Project</a> &nbsp;/&nbsp; Media Files</div>
  <div class="abs rule" style="top:210px"></div>

  <section>
    <h2 class="abs section-title" style="top:234px">Project Information</h2>
    <p class="abs section-desc" style="top:256px">Lorem ipsum dolor sit amet conse ctetur adipisicing elit, sed do eiusmod tempor incididunt ut labore et dolore magna</p>

    <span class="abs label" style="left:108px;top:307px;width:70px">First Name:</span>
    <div class="abs field" style="left:188px;top:304px;width:200px">First Name....</div>

    <span class="abs label" style="left:108px;top:351px;width:70px">Last Name:</span>
    <div class="abs field focus" style="left:188px;top:344px;width:200px">Merrow|</div>

    <span class="abs label" style="left:108px;top:394px;width:70px">Filename:</span>
    <div class="abs field" style="left:188px;top:387px;width:175px">Choose your file....</div>
    <div class="abs btn" style="left:362px;top:388px;width:26px;height:23px;font-weight:400">···</div>
    <div class="abs btn" style="left:420px;top:389px;width:55px">Upload</div>

    <span class="abs label" style="left:108px;top:439px;width:70px">Project Date:</span>
    <div class="abs field" style="left:188px;top:432px;width:120px">Feb - 26 - 2013</div>
    <svg class="abs" style="left:315px;top:437px" width="11" height="11" aria-label="Calendar"><rect x="0.5" y="1.5" width="10" height="9" fill="#fff" stroke="#3a7fd6"/><rect x="0.5" y="1.5" width="10" height="2.5" fill="#3a7fd6"/><rect x="3" y="6" width="2" height="2" fill="#3a7fd6"/><rect x="6" y="6" width="2" height="2" fill="#3a7fd6"/></svg>
  </section>

  <section>
    <h2 class="abs section-title" style="top:496px">Stimuli</h2>
    <p class="abs section-desc" style="top:518px">Lorem ipsum dolor sit amet conse ctetur adipisicing elit, sed do eiusmod tempor incididunt ut labore et dolore magna</p>

    <table class="abs stimuli-table">
      <thead><tr><th style="width:180px">Name</th><th style="width:210px">Interval</th><th style="width:145px">Type</th><th style="border-right:0"></th></tr></thead>
      <tbody>
        <tr class="odd"><td>Lorem ipsum</td><td>0:0.00 &nbsp;-&gt;&nbsp; 1:10:56</td><td>Positive</td><td style="border-right:0">
          <svg class="ico"><rect width="8" height="9" fill="#e0a040"/></svg><span class="row-action">Edit</span>&nbsp;&nbsp;
          <svg class="ico"><rect x="1" y="2" width="6" height="7" fill="#555"/><rect width="8" height="1.5" fill="#555"/></svg><span class="row-action">Remove</span></td></tr>
        <tr class="even"><td>Lorem ipsum</td><td>0:0.00 &nbsp;-&gt;&nbsp; 1:10:56</td><td>Positive</td><td style="border-right:0">
          <svg class="ico"><rect width="8" height="9" fill="#e0a040"/></svg><span class="row-action">Edit</span>&nbsp;&nbsp;
          <svg class="ico"><rect x="1" y="2" width="6" height="7" fill="#555"/><rect width="8" height="1.5" fill="#555"/></svg><span class="row-action">Remove</span></td></tr>
      </tbody>
    </table>

    <div class="abs add-panel"></div>
    <span class="abs panel-label" style="left:148px;top:699px">Name:</span>
    <span class="abs panel-label" style="left:298px;top:699px">Type:</span>
    <span class="abs panel-label" style="left:420px;top:699px">Start Time:</span>
    <span class="abs panel-label" style="left:554px;top:699px">End Time:</span>

    <div class="abs field" style="left:150px;top:715px;width:132px;background:#fff;height:23px">Name</div>
    <div class="abs field" style="left:300px;top:715px;width:101px;height:23px;background:linear-gradient(#f2f2f2,#dcdcdc);color:#444">Generic</div>
    <div class="abs" style="left:380px;top:716px;width:20px;height:21px;border-left:1px solid #c4c4c4"><svg width="20" height="21"><path d="M6 9 H13 L9.5 13 Z" fill="#444"/></svg></div>

    <div class="abs time-box" style="left:420px;top:717px">1</div><span class="abs unit" style="left:446px;top:723px">m</span>
    <div class="abs time-box" style="left:461px;top:717px">1</div><span class="abs unit" style="left:488px;top:723px">s</span>
    <div class="abs time-box" style="left:499px;top:717px">1</div><span class="abs unit" style="left:526px;top:723px">ms</span>

    <div class="abs time-box" style="left:554px;top:717px">1</div><span class="abs unit" style="left:580px;top:723px">m</span>
    <div class="abs time-box" style="left:595px;top:717px">1</div><span class="abs unit" style="left:622px;top:723px">s</span>
    <div class="abs time-box" style="left:634px;top:717px">1</div><span class="abs unit" style="left:661px;top:723px">ms</span>

    <div class="abs btn" style="left:709px;top:713px;width:53px">Save</div>
  </section>

  <section>
    <h2 class="abs section-title" style="top:809px">Survey Link</h2>
    <p class="abs section-desc" style="top:830px">Lorem ipsum dolor sit amet conse ctetur adipisicing elit, sed do eiusmod tempor incididunt ut labore et dolore magna</p>

    <span class="abs label" style="left:110px;top:880px;width:140px">Survey Link for this media file:</span>
    <div class="abs field" style="left:266px;top:872px;width:496px;height:26px;background:#e8e8e8;color:#555">http://www.surveyhall.example</div>
    <div class="abs btn" style="left:761px;top:872px;width:25px;height:26px"></div>

    <span class="abs label" style="left:150px;top:923px;width:100px">Link Properties:</span>
    <div class="abs check" style="left:265px;top:923px;background:transparent;border:0"><svg width="11" height="11"><path d="M1.5 5.5 L4.5 8.5 L10 2" stroke="#333" stroke-width="1.6" fill="none"/></svg></div>
    <span class="abs check-label" style="left:283px;top:924px">User ID</span>
    <div class="abs check" style="left:265px;top:944px"></div>
    <span class="abs check-label" style="left:283px;top:945px">Independent Variables</span>
    <div class="abs check" style="left:265px;top:966px"></div>
    <span class="abs check-label" style="left:283px;top:967px">Use in iframe</span>
  </section>

  <div class="abs rule" style="top:1027px"></div>
</main>

<footer>
  <div class="abs site-footer"></div>
  <div class="abs social" style="left:568px" role="img" aria-label="Social link"></div>
  <div class="abs social" style="left:595px" role="img" aria-label="Social link"></div>
  <div class="abs social" style="left:622px" role="img" aria-label="Social link"></div>
  <div class="abs footer-brand">gazemetric</div>
  <a class="abs footer-link" style="left:454px">Legal Notice</a>
  <a class="abs footer-link" style="left:532px">Sitemap</a>
  <a class="abs footer-link" style="left:594px">Contact Us</a>
  <span class="abs copyright">© 2013 Alan Merrow</span>
</footer>

</body>
</html>
```